Cleaning Service Company In need of Good Web presence.

The company is a cleaning service company which provides professional staff and service for cleaning. This is a project to build a site that is both solid and a strong recognition of our organization. It is supposed to show quality, cleanliness, professionalism. The use of images and art for imagery is all good just to have a site that is consistent and solid. There might be a chance to make stationary, logo and business cars if someone feels they can build a brand that is consistent. The image we are going for is clean solid and to stand out. Finally stationary should not be expensive to print.

Current logo is attached and can be used or can be made more creative.

Target Market(s)

Corporate and Government entities, that will feel that this company has a brand that sets it apart from the rest. The company is new so the modification of the logo will not be an issue if a more solid brand come out of this project. The idea is to have a clean consistent product that stands our from others in terms of website, stationary, etc

Industry/Entity Type

Cleaning Service

Contact Information for Business Card

P.O.Box 41967
Riffa
Kingdom of Bahrain

Logo Text

Maple Ridge Solutions

Number of Pages Required

4 page

Font styles to use
Sans Serif

Colors
abd036
cadf82
eaf2ce
9bcb3b

Requirements
Must have
• Green Color to be used in order to stick to the name. Also the creativity and boldness in an elegant manner.
Nice to have
• Arabic name of company
• نوفا بلو للحلول ذ.م.م
• if cannot be put at least make a location should be chosen
• Also could be a bit of 3D given to the logo if it could stay elegent.
Should not have
• Should not show people cleaning.

```html
<!DOCTYPE html>
<html lang="en">
<head>
<meta charset="utf-8">
<title>Maple Ridge Solutions W.L.L — Kingdom of Bahrain</title>
<link rel="stylesheet" href="https://fonts.googleapis.com/css2?family=Lato:wght@400;700;900&family=Raleway:wght@400;500;600&family=Open+Sans:wght@400&display=swap">
<style>
:root{
  --lime:#84c52c;
  --lime-soft:#9bcb3b;
  --forest:#0b7a3d;
  --forest-dark:#086a34;
  --card-dark:#2f7145;
  --ink:#1d1d1d;
  --grey:#555;
  --light-grey:#888;
  --field:#f2f2f2;
  --yellow:#e4f21e;
  --white:#fff;
}
*{box-sizing:border-box;margin:0;padding:0}
html,body{width:1200px;height:2663px;overflow:hidden;background:var(--white)}
body{position:relative;font-family:"Lato",Arial,sans-serif;color:var(--ink)}
.abs{position:absolute}

/* header */
.top-rule-left{left:0;top:0;width:585px;height:4px;background:var(--lime)}
.top-rule-right{left:592px;top:0;width:608px;height:4px;background:var(--forest)}
.brand{left:101px;top:27px;width:178px;height:178px;border-radius:50%;background:var(--white);border:8px solid var(--lime);z-index:3;display:flex;align-items:center;justify-content:center;text-align:center;font-weight:900;font-size:19px;line-height:1.2;color:var(--forest);padding:0 14px}
.nav{left:431px;top:48px;display:flex;font-size:14px;font-weight:700;text-transform:uppercase;white-space:nowrap}
.nav a{color:var(--ink);text-decoration:none;height:35px;line-height:35px;padding:0 13px;margin-right:8px}
.nav a.active{background:var(--lime);color:var(--white)}
.email{left:923px;top:24px;font-size:13px;color:var(--grey);white-space:nowrap}
.call-icon{left:882px;top:50px;width:30px;height:30px;background:var(--forest);display:flex;align-items:center;justify-content:center}
.call{left:920px;top:55px;font-size:15px;font-weight:700;color:var(--ink);white-space:nowrap}
.call span{color:var(--lime);font-weight:700}
.call-rule{left:915px;top:45px;width:190px;height:1px;background:#ddd}

/* hero */
.hero{left:0;top:108px;width:1200px;height:453px;background:linear-gradient(180deg,#2f6db3 0%,#5f9bd3 50%,#a9c9df 62%,#3d6a6a 80%,#1f4b3f 100%)}
.hero-title{left:107px;top:254px;font-size:34px;font-weight:700;color:#111;letter-spacing:.5px;white-space:nowrap}
.hero-badge{left:108px;top:302px;height:41px;background:var(--forest);color:var(--white);font-size:26px;font-weight:700;line-height:41px;padding:0 9px;letter-spacing:.3px;white-space:nowrap}

/* process */
.section-title{left:0;width:1200px;text-align:center;font-size:32px;font-weight:700;color:var(--ink);letter-spacing:.5px}
.process-intro{left:153px;top:696px;width:894px;text-align:center;font-size:16.5px;line-height:1.6;color:var(--grey);font-family:"Open Sans","Lato",Arial,sans-serif}
.steps{left:0;top:826px;width:1200px;height:300px}
.step-title{position:absolute;width:240px;text-align:center;font-family:Arial,sans-serif;font-weight:700;font-size:16px;color:var(--ink);top:208px}
.step-text{position:absolute;width:226px;text-align:center;font-family:Arial,sans-serif;font-size:12px;line-height:1.6;color:var(--grey);top:236px}

/* cta band */
.cta{left:0;top:1204px;width:577px;height:456px;background:var(--lime)}
.cta-title{left:99px;top:1270px;font-size:31px;font-weight:900;color:var(--white);letter-spacing:.3px;white-space:nowrap}
.cta-sub{left:102px;top:1322px;width:430px;font-size:13px;font-weight:700;line-height:1.75;color:var(--white);text-transform:uppercase}
.cta-lead{left:102px;top:1390px;width:440px;font-size:25px;font-weight:700;line-height:1.16;color:var(--white);text-transform:uppercase}
.cta-button{left:99px;top:1541px;width:315px;height:53px;background:var(--forest);color:var(--white);font-size:16px;font-weight:700;display:flex;align-items:center;justify-content:center;gap:14px;text-transform:uppercase;white-space:nowrap}
.cta-photo{left:577px;top:1204px;width:623px;height:456px;background:linear-gradient(135deg,#2f3d4c 0%,#3a4a5a 55%,#5b5148 78%,#a2502f 100%)}

/* testimonials */
.quote{font-family:"Raleway",Arial,sans-serif;color:var(--white);font-size:16px;line-height:1.8;padding:22px 58px 0}
.quote-light{left:172px;top:1837px;width:428px;height:133px;background:var(--lime)}
.quote-dark{left:579px;top:1862px;width:427px;height:135px;background:var(--card-dark)}
.avatar{width:40px;height:40px;border-radius:50%;background:#c9b8a8}
.person-name{font-family:"Raleway",Arial,sans-serif;font-size:16px;font-weight:500;color:var(--ink);white-space:nowrap}
.person-role{font-family:"Raleway",Arial,sans-serif;font-size:13px;color:var(--light-grey);white-space:nowrap}
.slider-arrow{width:42px;height:42px;border-radius:50%;border:1.5px solid #ddd;display:flex;align-items:center;justify-content:center}

/* footer */
.footer{left:0;top:2178px;width:1200px;height:485px;background:var(--forest)}
.footer-mark{left:579px;top:2217px;width:40px;height:5px;background:var(--yellow)}
.footer-title{left:0;top:2238px;width:1200px;text-align:center;font-family:Arial,sans-serif;font-size:23px;font-weight:700;color:var(--white);letter-spacing:-.5px}
.footer-copy{left:118px;top:2316px;width:440px;text-align:center;font-family:Arial,sans-serif;font-size:12px;font-weight:700;line-height:1.75;color:var(--white)}
.footer-address{left:118px;top:2376px;width:440px;text-align:center;font-family:Arial,sans-serif;font-size:12px;color:var(--white)}
.footer-phone{left:118px;top:2405px;width:440px;text-align:center;font-family:Arial,sans-serif;font-size:26px;font-weight:700;color:var(--white);display:flex;justify-content:center;align-items:center;gap:8px}
.footer-brand{left:283px;top:2452px;width:136px;height:136px;border-radius:50%;background:var(--white);border:6px solid var(--lime);display:flex;align-items:center;justify-content:center;text-align:center;font-weight:900;font-size:15px;line-height:1.2;color:var(--forest);padding:0 10px}
.field{left:612px;width:462px;background:var(--field);border:1px solid #ddd;font-family:Arial,sans-serif;font-size:12px;color:#999;padding:0 10px;display:flex;align-items:center}
.field-area{align-items:flex-start;padding-top:10px}
.quote-button{left:612px;top:2549px;width:125px;height:36px;background:var(--yellow);font-family:Arial,sans-serif;font-size:12px;font-weight:700;color:var(--forest-dark);display:flex;align-items:center;justify-content:center;text-transform:uppercase}
.footer-rule{left:114px;top:2613px;width:947px;height:1px;background:rgba(255,255,255,.18)}
.copyright{left:0;top:2629px;width:1200px;text-align:center;font-family:Arial,sans-serif;font-size:12px;color:var(--white)}
</style>
</head>
<body>

<header>
  <div class="abs top-rule-left"></div>
  <div class="abs top-rule-right"></div>
  <div class="abs brand">Maple Ridge Solutions</div>
  <nav class="abs nav">
    <a class="active">Home</a><a>About Us</a><a>Services</a><a>Blog</a><a>Contact</a>
  </nav>
  <div class="abs email">info@mapleridgesolutions.com</div>
  <div class="abs call-rule"></div>
  <div class="abs call-icon">
    <svg width="16" height="16" viewBox="0 0 24 24"><path fill="#fff" d="M6.6 10.8a15.1 15.1 0 0 0 6.6 6.6l2.2-2.2c.3-.3.7-.4 1-.2 1.1.4 2.3.6 3.6.6.6 0 1 .4 1 1V20c0 .6-.4 1-1 1A17 17 0 0 1 3 4c0-.6.4-1 1-1h3.5c.6 0 1 .4 1 1 0 1.3.2 2.5.6 3.6.1.3 0 .7-.2 1z"/></svg>
  </div>
  <div class="abs call">CALL: <span>+44 0455 812 097</span></div>
</header>

<section>
  <div class="abs hero" role="img" aria-label="Photograph of the Manama city skyline with twin sail-shaped towers over the waterfront under a blue sky"></div>
  <h1 class="abs hero-title">MAPLE RIDGE SOLUTIONS W.L.L</h1>
  <div class="abs hero-badge">KINGDOM OF BAHRAIN</div>
</section>

<section>
  <h2 class="abs section-title" style="top:633px">OUR CLEANING PROCESS</h2>
  <p class="abs process-intro">Lorem ipsum dolor sit amet, consectetur adipisicing elit, sed do eiusmod tempor incididunt ut labore et dolore magna aliqua. Ut enim ad minim veniam.</p>

  <div class="abs steps">
    <svg width="1200" height="200" viewBox="0 0 1200 200" style="position:absolute;left:0;top:0">
      <g fill="none" stroke="#84c52c" stroke-width="10">
        <circle cx="220" cy="95" r="80"/><circle cx="470" cy="95" r="80"/>
        <circle cx="721" cy="95" r="80"/><circle cx="971" cy="95" r="80"/>
      </g>
      <g fill="none" stroke="#666" stroke-width="2">
        <path d="M323 92h42M355 84l10 8-10 8"/>
        <path d="M574 92h42M606 84l10 8-10 8"/>
        <path d="M824 92h42M856 84l10 8-10 8"/>
      </g>
      <g fill="#0b7a3d">
        <circle cx="165" cy="35" r="23"/><circle cx="415" cy="35" r="23"/>
        <circle cx="666" cy="35" r="23"/><circle cx="916" cy="35" r="23"/>
      </g>
      <g fill="#fff" font-family="Lato,Arial,sans-serif" font-weight="700" font-size="20" text-anchor="middle">
        <text x="165" y="42">1</text><text x="415" y="42">2</text>
        <text x="666" y="42">3</text><text x="916" y="42">4</text>
      </g>
      <g fill="none" stroke="#333" stroke-width="2" stroke-linejoin="round" stroke-linecap="round">
        <path d="M204 76c-3 2-3 8 2 16s13 16 21 19c5 2 9 0 11-3l-7-7-5 3c-4-2-9-7-11-11l3-5z"/>
        <path d="M221 78a14 14 0 0 1 14 14M221 71a21 21 0 0 1 21 21"/>
        <rect x="448" y="75" width="44" height="40" rx="3"/><path d="M448 87h44M458 69v10M482 69v10M460 101l7 6 13-13"/>
        <path d="M706 112h22a8 8 0 0 0 0-16h-8l-6-24a5 5 0 0 0-9 2l4 22"/><circle cx="708" cy="114" r="3"/>
        <rect x="952" y="80" width="40" height="26" rx="3" transform="rotate(-15 972 93)"/><path d="M952 90l38-10"/>
      </g>
    </svg>
    <div class="step-title" style="left:100px">Give us a Call</div>
    <div class="step-text" style="left:107px">Phasellus ac tincidunt eros. Nulla egestas tristique turpis sit amet lobortis</div>
    <div class="step-title" style="left:350px">Schedule it</div>
    <div class="step-text" style="left:357px">Phasellus ac tincidunt eros. Nulla egestas tristique turpis sit amet lobortis</div>
    <div class="step-title" style="left:601px">The Cleaning</div>
    <div class="step-text" style="left:608px">Phasellus ac tincidunt eros. Nulla egestas tristique turpis sit amet lobortis</div>
    <div class="step-title" style="left:851px">Easy Payment</div>
    <div class="step-text" style="left:858px">Phasellus ac tincidunt eros. Nulla egestas tristique turpis sit amet lobortis</div>
  </div>
</section>

<section>
  <div class="abs cta"></div>
  <h2 class="abs cta-title">OUR CLEANING PROCESS</h2>
  <p class="abs cta-sub">If you're tired of fighting all the dirt at your home or office all by yourself, then call us!</p>
  <p class="abs cta-lead">We're experienced in turning the messiest places around and turning them to real cleanliness havens!</p>
  <div class="abs cta-button">Book an Appointment
    <svg width="20" height="20" viewBox="0 0 20 20"><circle cx="10" cy="10" r="10" fill="#fff"/><path d="M8 5l5 5-5 5" fill="none" stroke="#0b7a3d" stroke-width="2.5"/></svg>
  </div>
  <div class="abs cta-photo" role="img" aria-label="Photograph of a vacuum cleaner nozzle on dark carpet beside a wooden door"></div>
</section>

<section>
  <h2 class="abs section-title" style="top:1742px;font-size:31px">CLIENT TESTIMONIALS</h2>
  <div class="abs slider-arrow" style="left:86px;top:1942px"><svg width="12" height="12" viewBox="0 0 12 12"><path d="M8 1L3 6l5 5" fill="none" stroke="#ccc" stroke-width="1.5"/></svg></div>
  <div class="abs slider-arrow" style="left:1074px;top:1942px"><svg width="12" height="12" viewBox="0 0 12 12"><path d="M4 1l5 5-5 5" fill="none" stroke="#ccc" stroke-width="1.5"/></svg></div>

  <div class="abs quote-light"><p class="quote">Lorem ipsum dolor sit amet, consectetur adipisicing elit. Enim, delectus atque odit esse harum! Saepe!</p></div>
  <svg class="abs" style="left:462px;top:1969px" width="28" height="28" viewBox="0 0 28 28"><path d="M0 0h28L0 28z" fill="#84c52c"/></svg>
  <div class="abs avatar" style="left:198px;top:2000px"></div>
  <div class="abs person-name" style="left:254px;top:1998px">John Doe</div>
  <div class="abs person-role" style="left:249px;top:2024px">Web designer</div>

  <div class="abs quote-dark"><p class="quote">Lorem ipsum dolor sit amet, consectetur adipisicing elit. Enim, delectus atque odit esse harum! Saepe!</p></div>
  <svg class="abs" style="left:869px;top:1996px" width="26" height="26" viewBox="0 0 26 26"><path d="M0 0h26L0 26z" fill="#2f7145"/></svg>
  <div class="abs avatar" style="left:605px;top:2025px"></div>
  <div class="abs person-name" style="left:655px;top:2023px">Jessica Doe</div>
  <div class="abs person-role" style="left:669px;top:2050px">Developer</div>
</section>

<footer>
  <div class="abs footer"></div>
  <div class="abs footer-mark"></div>
  <h2 class="abs footer-title">Get In Touch</h2>
  <p class="abs footer-copy">We are determined to carry on our mission for as long as there will be a demand for that kind of care!</p>
  <p class="abs footer-address">14 Cedar Lane Riffa 90210, Bahrain</p>
  <div class="abs footer-phone">
    <svg width="22" height="22" viewBox="0 0 24 24"><path fill="#e4f21e" d="M6.6 10.8a15.1 15.1 0 0 0 6.6 6.6l2.2-2.2c.3-.3.7-.4 1-.2 1.1.4 2.3.6 3.6.6.6 0 1 .4 1 1V20c0 .6-.4 1-1 1A17 17 0 0 1 3 4c0-.6.4-1 1-1h3.5c.6 0 1 .4 1 1 0 1.3.2 2.5.6 3.6.1.3 0 .7-.2 1z"/></svg>
    800-4172-3950
  </div>
  <div class="abs footer-brand">Maple Ridge Solutions</div>

  <div class="abs field" style="top:2320px;height:37px">Full Name...</div>
  <div class="abs field" style="top:2370px;height:37px">Enter Address...</div>
  <div class="abs field field-area" style="top:2421px;height:114px">Write message</div>
  <div class="abs quote-button">Ask a Quote</div>

  <div class="abs footer-rule"></div>
  <p class="abs copyright">© 2017 Maple Ridge Solutions W.L.L All Rights Reserved</p>
</footer>

</body>
</html>
```